christmas trees postcard design

wales largest grower of christmas trees, suppling freshly cut perfect christmas trees, wholesale, retail businesses and nmb 27 marlow terrace! Our focus in nurturing the perfect christmas tree from seed for 10 years , and providing a fresh long lasting christmas tree which lasts the festive period, trees from 2 ft to 20ft , many varieties sixzes and shapes

```html
<!DOCTYPE html>
<html lang="en">
<head>
<meta charset="utf-8">
<title>Christmas Trees Postcards</title>
<link href="https://fonts.googleapis.com/css2?family=Pathway+Gothic+One&family=Great+Vibes&display=swap" rel="stylesheet">
<style>
  :root {
    --bg: #ecebea;
    --card: #ffffff;
    --green: #1f6b3c;
    --red: #d7141f;
    --snow-light: #eef1f4;
    --snow-mid: #c9d2d8;
    --pine: #3e5a4a;
    --frame-green: #1e6a36;
    --frame-red: #d9141c;
  }
  * { margin: 0; padding: 0; box-sizing: border-box; }
  html, body { width: 1200px; height: 772px; overflow: hidden; background: var(--bg); }
  .canvas {
    position: relative; width: 1200px; height: 772px;
    display: grid; grid-template-columns: 460px 460px; grid-template-rows: 353px 353px;
    gap: 30px 40px; padding: 18px 120px;
  }
  .postcard { position: relative; background: var(--card); overflow: hidden; box-shadow: 0 4px 12px rgba(0,0,0,.18); }
  .postcard--green { border: 12px solid var(--frame-green); }
  .postcard--red { border: 12px solid var(--frame-red); background: var(--frame-red); }

  .photo { position: absolute; }
  .photo--snowfield { background: linear-gradient(180deg, #dfe3e6 0%, #f3f4f5 30%, #6d7f74 45%, #3e5a4a 62%, #e9edf0 82%, #f7f8f9 100%); }
  .photo--grower { background: linear-gradient(180deg, #5e7a58 0%, #2f4a32 55%, #9aa39a 100%); }
  .photo--path { background: linear-gradient(180deg, #a9bccb 0%, #40594b 40%, #dfe6ec 75%, #f5f7f9 100%); }

  .message {
    position: absolute; background: var(--card);
    display: flex; flex-direction: column; align-items: center; justify-content: center;
    color: var(--green); font-family: "Pathway Gothic One", sans-serif; text-align: center; line-height: 1;
  }
  .message__icons { display: flex; align-items: center; gap: 14px; margin-bottom: 6px; }
  .message__small { font-size: 17px; letter-spacing: 2px; }
  .message__mid { font-size: 22px; letter-spacing: 2px; margin-top: 2px; }
  .message__big { font-size: 40px; letter-spacing: 3px; }
  .message__script { font-family: "Great Vibes", cursive; font-size: 42px; letter-spacing: 0; margin: -4px 0 -2px; }
  .message--wide .message__big { font-size: 42px; }
  .message--wide .message__caps { font-size: 30px; letter-spacing: 2px; margin-top: 2px; }
</style>
</head>
<body>
<main class="canvas">

  <!-- Design A: white -->
  <section class="postcard">
    <div class="message" style="left:0;top:0;width:40%;height:100%;">
      <div class="message__icons">
        <svg width="16" height="16" viewBox="-8 -8 16 16"><g stroke="var(--green)" stroke-width="2"><line x1="-7" y1="0" x2="7" y2="0"/><line x1="-3.5" y1="-6" x2="3.5" y2="6"/><line x1="3.5" y1="-6" x2="-3.5" y2="6"/></g></svg>
        <svg width="20" height="22" viewBox="0 0 20 22"><rect x="8" y="0" width="4" height="4" fill="#b5b5b5"/><circle cx="10" cy="13" r="9" fill="var(--red)"/></svg>
        <svg width="16" height="16" viewBox="-8 -8 16 16"><g stroke="var(--green)" stroke-width="2"><line x1="-7" y1="0" x2="7" y2="0"/><line x1="-3.5" y1="-6" x2="3.5" y2="6"/><line x1="3.5" y1="-6" x2="-3.5" y2="6"/></g></svg>
      </div>
      <span class="message__small">PROVIDING</span>
      <span class="message__mid">FRESHLY CUT</span>
      <span class="message__big">PERFECT</span>
      <span class="message__script">christmas</span>
      <span class="message__big">TREES</span>
    </div>
    <div class="photo photo--snowfield" role="img" aria-label="Photo of rows of snow-covered christmas trees on a hillside" style="left:40%;top:0;width:60%;height:100%;"></div>
  </section>

  <!-- Design B: green frame -->
  <section class="postcard postcard--green">
    <div class="message" style="left:0;top:0;width:40%;height:100%;">
      <div class="message__icons">
        <svg width="16" height="16" viewBox="-8 -8 16 16"><g stroke="var(--green)" stroke-width="2"><line x1="-7" y1="0" x2="7" y2="0"/><line x1="-3.5" y1="-6" x2="3.5" y2="6"/><line x1="3.5" y1="-6" x2="-3.5" y2="6"/></g></svg>
        <svg width="20" height="22" viewBox="0 0 20 22"><rect x="8" y="0" width="4" height="4" fill="#b5b5b5"/><circle cx="10" cy="13" r="9" fill="var(--red)"/></svg>
        <svg width="16" height="16" viewBox="-8 -8 16 16"><g stroke="var(--green)" stroke-width="2"><line x1="-7" y1="0" x2="7" y2="0"/><line x1="-3.5" y1="-6" x2="3.5" y2="6"/><line x1="3.5" y1="-6" x2="-3.5" y2="6"/></g></svg>
      </div>
      <span class="message__small">PROVIDING</span>
      <span class="message__mid">FRESHLY CUT</span>
      <span class="message__big">PERFECT</span>
      <span class="message__script">christmas</span>
      <span class="message__big">TREES</span>
    </div>
    <div class="photo photo--snowfield" role="img" aria-label="Photo of rows of snow-covered christmas trees on a hillside" style="left:40%;top:0;width:60%;height:100%;"></div>
  </section>

  <!-- Design C: white collage -->
  <section class="postcard">
    <div class="message message--wide" style="left:0;top:0;width:70%;height:46%;">
      <div class="message__icons" style="gap:60px;">
        <svg width="16" height="16" viewBox="-8 -8 16 16"><g stroke="var(--green)" stroke-width="2"><line x1="-7" y1="0" x2="7" y2="0"/><line x1="-3.5" y1="-6" x2="3.5" y2="6"/><line x1="3.5" y1="-6" x2="-3.5" y2="6"/></g></svg>
        <svg width="20" height="22" viewBox="0 0 20 22"><rect x="8" y="0" width="4" height="4" fill="#b5b5b5"/><circle cx="10" cy="13" r="9" fill="var(--red)"/></svg>
        <svg width="16" height="16" viewBox="-8 -8 16 16"><g stroke="var(--green)" stroke-width="2"><line x1="-7" y1="0" x2="7" y2="0"/><line x1="-3.5" y1="-6" x2="3.5" y2="6"/><line x1="3.5" y1="-6" x2="-3.5" y2="6"/></g></svg>
      </div>
      <span class="message__small">PROVIDING</span>
      <span class="message__mid">FRESHLY CUT</span>
      <span class="message__big">PERFECT</span>
      <span class="message__caps">CHRISTMAS TREES</span>
    </div>
    <div class="photo photo--snowfield" role="img" aria-label="Photo of a snowy plantation of young christmas trees" style="left:0;top:46%;width:70%;height:54%;"></div>
    <div class="photo photo--grower" role="img" aria-label="Photo of the grower standing beside a tall christmas tree" style="left:72%;top:3%;width:26%;height:46%;"></div>
    <div class="photo photo--path" role="img" aria-label="Photo of a snowy path between rows of christmas trees" style="left:72%;top:51%;width:26%;height:46%;"></div>
  </section>

  <!-- Design D: red frame collage -->
  <section class="postcard postcard--red">
    <div class="message message--wide" style="left:0;top:0;width:69%;height:46%;">
      <div class="message__icons" style="gap:60px;">
        <svg width="16" height="16" viewBox="-8 -8 16 16"><g stroke="var(--green)" stroke-width="2"><line x1="-7" y1="0" x2="7" y2="0"/><line x1="-3.5" y1="-6" x2="3.5" y2="6"/><line x1="3.5" y1="-6" x2="-3.5" y2="6"/></g></svg>
        <svg width="20" height="22" viewBox="0 0 20 22"><rect x="8" y="0" width="4" height="4" fill="#b5b5b5"/><circle cx="10" cy="13" r="9" fill="var(--red)"/></svg>
        <svg width="16" height="16" viewBox="-8 -8 16 16"><g stroke="var(--green)" stroke-width="2"><line x1="-7" y1="0" x2="7" y2="0"/><line x1="-3.5" y1="-6" x2="3.5" y2="6"/><line x1="3.5" y1="-6" x2="-3.5" y2="6"/></g></svg>
      </div>
      <span class="message__small">PROVIDING</span>
      <span class="message__mid">FRESHLY CUT</span>
      <span class="message__big">PERFECT</span>
      <span class="message__caps">CHRISTMAS TREES</span>
    </div>
    <div class="photo photo--snowfield" role="img" aria-label="Photo of a snowy plantation of young christmas trees" style="left:0;top:46%;width:69%;height:54%;"></div>
    <div class="photo photo--grower" role="img" aria-label="Photo of the grower standing beside a tall christmas tree" style="left:72%;top:0;width:28%;height:48.5%;"></div>
    <div class="photo photo--path" role="img" aria-label="Photo of a snowy path between rows of christmas trees" style="left:72%;top:51.5%;width:28%;height:48.5%;"></div>
  </section>

</main>
</body>
</html>
```